Stationery Set for new venture capital firm

We need a new set of stationery including letterhead, business cards, envelopes, with compliment slips for our new startup venture capital firm known as Halvora.
We make alternative investments globally and hope to have a worldwide network of offices later.

The stationery should be elegant and not too fussy with the use of too many colors.

Venture Capital

```html
<!DOCTYPE html>
<html lang="en">
<head>
<meta charset="utf-8">
<title>Halvora — Business Card</title>
<link href="https://fonts.googleapis.com/css2?family=Arimo:wght@400;700&display=swap" rel="stylesheet">
<style>
  :root {
    --backdrop: #2a2a2a;
    --card-white: #ffffff;
    --card-fade: #ececec;
    --brand-blue: #2399d4;
    --brand-blue-deep: #1c86bd;
    --brand-blue-tone: #1e8cc4;
    --ink-grey: #6d6e70;
    --ink-soft: #8a8b8d;
  }
  * { margin: 0; padding: 0; box-sizing: border-box; }
  html, body { width: 1200px; height: 900px; overflow: hidden; }
  body {
    background: var(--backdrop);
    font-family: "Arimo", Helvetica, Arial, sans-serif;
    position: relative;
  }
  .card {
    position: absolute;
    top: 307px;
    width: 500px;
    height: 286px;
  }
  .card-front {
    left: 70px;
    background: linear-gradient(180deg, var(--card-white) 0%, var(--card-fade) 100%);
  }
  .card-back {
    left: 630px;
    background: var(--brand-blue);
  }

  /* front */
  .brand-lockup {
    position: absolute;
    left: 44px;
    top: 56px;
    display: flex;
    align-items: center;
    gap: 10px;
  }
  .brand-dot {
    width: 22px; height: 22px;
    border-radius: 50%;
    background: var(--brand-blue);
  }
  .brand-name {
    font-weight: 700;
    font-size: 34px;
    color: var(--ink-grey);
    letter-spacing: -0.5px;
  }
  .front-web {
    position: absolute;
    left: 44px;
    bottom: 36px;
    font-size: 12px;
    color: var(--brand-blue);
  }
  .front-band {
    position: absolute;
    left: 0; right: 0; bottom: 0;
    height: 18px;
    background: var(--brand-blue-deep);
  }
  .person {
    position: absolute;
    left: 270px;
    top: 58px;
  }
  .person-name {
    font-size: 17px;
    color: var(--brand-blue);
  }
  .person-title {
    font-size: 10px;
    color: var(--brand-blue);
    letter-spacing: 0.6px;
    margin-top: 2px;
  }
  .contact {
    position: absolute;
    left: 270px;
    top: 118px;
    list-style: none;
    font-size: 11px;
    line-height: 16px;
    color: var(--ink-soft);
  }
  .contact b {
    display: inline-block;
    width: 12px;
    color: var(--brand-blue);
    font-weight: 700;
  }
  .address {
    position: absolute;
    left: 270px;
    top: 180px;
    font-style: normal;
    font-size: 11px;
    line-height: 16px;
    color: var(--ink-soft);
  }

  /* back */
  .back-lockup {
    position: absolute;
    left: 0; right: 0;
    top: 100px;
    display: flex;
    justify-content: center;
    align-items: center;
    gap: 12px;
  }
  .back-dot {
    width: 28px; height: 28px;
    border-radius: 50%;
    background: var(--brand-blue-tone);
  }
  .back-name {
    font-weight: 700;
    font-size: 48px;
    color: var(--brand-blue-tone);
    letter-spacing: -0.5px;
  }
  .back-web {
    position: absolute;
    left: 0; right: 0;
    bottom: 44px;
    text-align: center;
    font-size: 15px;
    color: var(--card-white);
  }
</style>
</head>
<body>
  <section class="card card-front" aria-label="Business card front">
    <div class="brand-lockup">
      <span class="brand-dot"></span>
      <span class="brand-name">Halvora</span>
    </div>
    <div class="person">
      <div class="person-name">Mirela Castano</div>
      <div class="person-title">MANAGER</div>
    </div>
    <ul class="contact">
      <li><b>t</b>+852 2400 1170</li>
      <li><b>f</b>+852 2400 1171</li>
      <li><b>e</b>castano@thehalvoragroup.com</li>
    </ul>
    <address class="address">
      18th Floor, Linden Tower<br>
      7 Quay Road<br>
      Hong Kong
    </address>
    <div class="front-web">www.thehalvoragroup.com</div>
    <div class="front-band"></div>
  </section>

  <section class="card card-back" aria-label="Business card back">
    <div class="back-lockup">
      <span class="back-dot"></span>
      <span class="back-name">Halvora</span>
    </div>
    <div class="back-web">www.thehalvoragroup.com</div>
  </section>
</body>
</html>
```